Sustainable, ethical bath and beauty care product business needs a Shopify website design.

E-commerce site for environmentally friendly bath and beauty care products company. Our mantra is 'Relax, Re-energize, Reinvent' and and we would like the site to reflect those concepts. We'd like a clean and classy website with rustic and natural nuances. We are also hoping to creatively connect our products to the 5 senses in some way. Looking for retail and wholesale accounts options.
Updates

Target Market(s)

Beauty Industry

Industry/Entity Type

Beauty

Coding

Coded - Design and coding required

Colors
EE7325
F08F49
F5BC92
FAE3D3
FDF4ED
6B429C
8869AF
B7A5CE
E3DAEB
F3F0F8

Requirements
Must have
• Sliding Banner included is the of the tree we submitted.

```html
<!DOCTYPE html>
<html lang="en">
<head>
<meta charset="utf-8">
<title>Lumera Naturals – Home</title>
<link rel="stylesheet" href="https://fonts.googleapis.com/css2?family=Merriweather:wght@700;900&family=Poppins:wght@600;700&family=Roboto:wght@400;500&display=swap">
<style>
:root{
  --orange:#ee7325;
  --orange-soft:#f08f49;
  --purple:#5c3382;
  --purple-deep:#6b429c;
  --purple-light:#b7a5ce;
  --ink:#1c1c1c;
  --muted:#444;
  --gold:#c9971c;
  --board:#8a8787;
  --white:#fff;
}
*{box-sizing:border-box;margin:0;padding:0}
html,body{width:895px;height:1200px;overflow:hidden;background:var(--board)}
body{font-family:"Roboto",Arial,sans-serif;color:var(--ink)}
.board{position:absolute;left:0;top:0;width:1652px;height:2214px;background:var(--board);transform:scale(0.54177);transform-origin:0 0}
.page{position:absolute;top:98px;width:687px;height:2010px;background:var(--white);overflow:hidden}
.page-home{left:106px}
.page-menu{left:845px}
.abs{position:absolute}

.topbar{left:0;top:0;width:687px;height:24px;background:var(--purple);color:#fff;font-size:8px;text-align:center;line-height:24px}
.brand{display:flex;align-items:center;gap:6px;font-family:"Merriweather",Georgia,serif;font-weight:700;font-size:12px;letter-spacing:2px;color:var(--purple)}
.brand-dot{width:12px;height:12px;border-radius:50%;background:var(--orange)}
.header-brand{left:68px;top:42px}
.search{left:265px;top:38px;width:215px;height:26px;border:1px solid #666;border-radius:2px;font-size:7.5px;padding:0 9px;display:flex;align-items:center;justify-content:space-between}
.icon-dot{width:18px;height:18px;border-radius:50%;background:var(--orange);display:flex;align-items:center;justify-content:center}
.btn{background:var(--orange);color:#fff;border-radius:12px;font-family:"Merriweather",Georgia,serif;font-weight:700;font-size:8px;display:flex;align-items:center;justify-content:center;box-shadow:0 2px 4px rgba(238,115,37,.35)}
.login{left:559px;top:40px;width:64px;height:21px}
.rule{left:64px;top:75px;width:558px;height:1px;background:#bbb}
.nav{top:84px;font-size:8.5px;color:var(--ink)}
.nav.active{color:var(--purple-deep);font-weight:500}

.hero{left:0;top:104px;width:687px;height:331px;background:linear-gradient(180deg,#f6b5aa 0%,#f4b1a6 54%,#c9d2d2 55%,#c9d2d2 76%,#d6cac0 77%,#e6ddd5 100%)}
.hero-title{left:0;top:138px;width:758px;text-align:center;font-family:"Poppins",Arial,sans-serif;font-weight:700;font-size:21px;line-height:29px;color:#111}
.hero-title span{color:var(--purple-deep)}
.hero-sub{left:0;top:201px;width:758px;text-align:center;font-size:8px}
.hero-btn{left:337px;top:226px;width:83px;height:20px}
.arrow{width:21px;height:21px;border-radius:50%;background:var(--orange);display:flex;align-items:center;justify-content:center}

.section-title{left:0;width:687px;text-align:center;font-family:"Merriweather",Georgia,serif;font-weight:900;font-size:15.5px;color:#111}
.section-title span{color:var(--purple-deep)}
.mantra-icon{width:68px;height:62px;background:var(--purple);border-radius:2px;box-shadow:0 3px 0 #3f1f5e;display:flex;align-items:center;justify-content:center}
.mantra-label{width:120px;text-align:center}
.mantra-label b{display:block;font-family:"Merriweather",Georgia,serif;font-size:10.5px;color:var(--purple-deep)}
.mantra-label small{display:block;font-size:7.5px;margin-top:3px;color:#222}

.band{left:0;width:687px;height:231px;background:var(--purple)}
.band-copy{color:#fff}
.band-copy h3{font-family:"Merriweather",Georgia,serif;font-weight:700;font-size:16px;margin-bottom:8px}
.band-copy p{font-size:7.6px;line-height:12px;text-align:justify}

.card{width:138px;background:#fff;box-shadow:0 2px 8px rgba(0,0,0,.18);display:flex;flex-direction:column;align-items:center;padding:14px 12px 18px}
.shot{width:100%;flex:1;border-radius:4px;margin-bottom:10px}
.card-name{font-family:"Merriweather",Georgia,serif;font-weight:700;font-size:10.5px}
.price{font-size:8px;margin-top:5px;font-family:"Merriweather",Georgia,serif}
.stars{color:var(--gold);font-size:8px;letter-spacing:3px;margin-top:5px}
.buy{width:62px;height:20px;margin-top:6px}
.quick{right:10px;display:flex;flex-direction:column;gap:8px}
.quick .icon-dot{width:17px;height:17px}

.badge{width:64px;height:64px;border-radius:50%;background:var(--purple);border:3px solid #fff;box-shadow:0 0 0 2px var(--purple);display:flex;align-items:center;justify-content:center}
.badge-label{width:100px;text-align:center;font-family:"Merriweather",Georgia,serif;font-weight:700;font-size:10.5px;color:var(--purple-deep)}

.quote-text{left:150px;top:1546px;width:420px;text-align:center;font-size:8.2px;line-height:15px}
.quote-mark{font-family:"Merriweather",Georgia,serif;font-weight:900;font-size:42px;color:var(--purple-light);line-height:1}
.avatar{border-radius:50%}
.person{left:0;width:720px;text-align:center}
.dots{left:346px;top:1740px;display:flex;gap:5px}
.dots i{width:7px;height:7px;border-radius:50%;background:#111;display:block}
.dots i.on{background:var(--orange)}

.footer{left:0;top:1796px;width:687px;height:214px;background:var(--purple);color:#fff}
.f-head{font-family:"Merriweather",Georgia,serif;font-weight:700;font-size:11px}
.f-list{font-size:8px;line-height:16.7px}
.f-list .on{font-weight:500}
.f-text{font-size:8px;line-height:16px}
.contact{display:flex;gap:6px;font-size:8px;line-height:13px}
.contact .icon-dot{width:12px;height:12px;flex:none;margin-top:1px}
.f-search{left:485px;top:1848px;width:137px;height:22px;border:1px solid #fff;font-size:6.5px;padding:0 8px;display:flex;align-items:center;justify-content:space-between}
.social{width:17px;height:17px;border-radius:50%;border:1px solid #fff}
.f-rule{left:64px;top:1968px;width:558px;height:1px;background:rgba(255,255,255,.35)}
.copy{left:0;top:1981px;width:687px;text-align:center;font-size:8px}

.dim{left:0;top:0;width:687px;height:2010px;background:rgba(20,15,20,.48)}
.mega{left:63px;top:104px;width:559px;height:205px;background:linear-gradient(135deg,#fdfbf9,#f7f1ec 60%,#fbf8f5)}
.mega-col h4{font-family:"Merriweather",Georgia,serif;font-weight:700;font-size:10.5px;margin-bottom:6px}
.mega-col li{list-style:none;font-family:"Merriweather",Georgia,serif;font-size:7.5px;line-height:16.3px;color:#333}
.ico{fill:none;stroke:#fff;stroke-width:2;stroke-linecap:round;stroke-linejoin:round}
</style>
</head>
<body>
<div class="board">

<!-- ============ HOME PAGE ============ -->
<div class="page page-home">
  <div class="abs topbar">Lorem ipsum dolor sit amet, consectetur adipiscing elit, sed do eiusmod</div>

  <div class="abs brand header-brand"><span class="brand-dot"></span>LUMERA</div>
  <div class="abs search"><span>All Categories ⌄</span>
    <svg width="8" height="8" viewBox="0 0 10 10"><circle cx="4" cy="4" r="3" fill="none" stroke="#333" stroke-width="1.4"/><path d="M6.3 6.3L9 9" stroke="#333" stroke-width="1.4"/></svg></div>
  <div class="abs icon-dot" style="left:505px;top:42px"><svg width="9" height="8" viewBox="0 0 10 9"><path d="M5 8.5L1 4.6A2.3 2.3 0 0 1 5 1.8a2.3 2.3 0 0 1 4 2.8z" fill="#fff"/></svg></div>
  <div class="abs icon-dot" style="left:531px;top:42px"><svg width="9" height="8" viewBox="0 0 10 9"><path d="M0 1h2l1.2 5h5L9.5 2.5H3" fill="none" stroke="#fff" stroke-width="1.3"/><circle cx="4" cy="8" r=".9" fill="#fff"/><circle cx="7.5" cy="8" r=".9" fill="#fff"/></svg></div>
  <div class="abs btn login">LOG IN</div>
  <div class="abs rule"></div>
  <div class="abs nav active" style="left:177px">Home</div>
  <div class="abs nav" style="left:233px">Bath</div>
  <div class="abs nav" style="left:282px">Body</div>
  <div class="abs nav" style="left:332px">Face</div>
  <div class="abs nav" style="left:381px">Candles</div>
  <div class="abs nav" style="left:444px">Kids</div>
  <div class="abs nav" style="left:492px">Pets</div>

  <div class="abs hero" role="img" aria-label="Banner photo: bright bathroom with a freestanding tub, plant, towel and small side table"></div>
  <div class="abs hero-title">WELCOME TO <span>LUMERA</span><br>NATURALS</div>
  <div class="abs hero-sub">All About Sustainable beauty Products</div>
  <div class="abs btn hero-btn">GET STARTED</div>
  <div class="abs arrow" style="left:17px;top:258px"><svg width="7" height="8" viewBox="0 0 7 8"><path d="M5 1L2 4l3 3" fill="none" stroke="#fff" stroke-width="1.5"/></svg></div>
  <div class="abs arrow" style="left:645px;top:258px"><svg width="7" height="8" viewBox="0 0 7 8"><path d="M2 1l3 3-3 3" fill="none" stroke="#fff" stroke-width="1.5"/></svg></div>

  <div class="abs section-title" style="top:480px">OUR <span>MANTRA</span></div>
  <div class="abs mantra-icon" style="left:115px;top:527px" role="img" aria-label="Relax icon">
    <svg width="42" height="42" viewBox="0 0 40 40"><circle cx="20" cy="8" r="4" fill="#fff"/><path d="M20 13c-4 0-6 3-6 8v4h12v-4c0-5-2-8-6-8z" fill="#fff"/><path class="ico" d="M14 17l-6 6 5 2M26 17l6 6-5 2"/><path d="M6 31c4-4 9-5 14-5s10 1 14 5c-5 2-9 2-14 1-5 1-9 1-14-1z" fill="#fff"/></svg></div>
  <div class="abs mantra-icon" style="left:305px;top:527px" role="img" aria-label="Re-energize icon">
    <svg width="44" height="44" viewBox="0 0 40 40" class="ico" style="stroke-width:1.6"><circle cx="24" cy="8" r="3"/><path d="M24 1.5v2M24 12.5v2M17.5 8h2M28.5 8h2M19.5 3.5l1.3 1.3M27.2 11.2l1.3 1.3M28.5 3.5l-1.3 1.3M19.5 12.5l1.3-1.3"/><path d="M9 22c0-3 2-4 4-4h14c2 0 4 1 4 4"/><path d="M5 22h30v5H5zM8 27v7M32 27v7M5 31h30"/></svg></div>
  <div class="abs mantra-icon" style="left:496px;top:527px" role="img" aria-label="Reinvent icon">
    <svg width="42" height="42" viewBox="0 0 40 40" class="ico" style="stroke-width:1.7"><path d="M20 4a11 11 0 0 0-6 20c1 1 2 3 2 5h8c0-2 1-4 2-5a11 11 0 0 0-6-20z"/><path d="M16 33h8M17 36h6"/><path d="M23 11.5c-.8-1-1.8-1.5-3-1.5-2 0-3 1-3 2.5 0 3.5 6 2 6 5.5 0 1.5-1.4 2.5-3 2.5-1.4 0-2.5-.6-3.3-1.5M20 7.5v2.5M20 20.5v2"/></svg></div>
  <div class="abs mantra-label" style="left:89px;top:596px"><b>Relax</b><small>Sustainably</small></div>
  <div class="abs mantra-label" style="left:279px;top:596px"><b>Re-Energize</b><small>Maskfully crafted</small></div>
  <div class="abs mantra-label" style="left:470px;top:596px"><b>Reinvent</b><small>Reinvent</small></div>

  <div class="abs band" style="top:710px"></div>
  <div class="abs band-copy" style="left:28px;top:780px;width:155px"><h3>Featured Products</h3><p>Lorem ipsum dolor sit amet, consectetur adipiscing elit, sed do eiusmod tempor incididunt ut labore et</p></div>
  <div class="abs card" style="left:200px;top:678px;height:212px">
    <div class="shot" role="img" aria-label="Product photo: coloured bath crayons" style="background:linear-gradient(135deg,#fff,#e9eef5 40%,#f6e7c3)"></div>
    <div class="card-name">Bath Caryans</div><div class="price">$ 30.00</div><div class="stars">★★★★★</div><div class="btn buy">Buy Now</div>
  </div>
  <div class="abs card" style="left:348px;top:663px;height:252px">
    <div class="shot" role="img" aria-label="Product photo: lipbalm tube" style="background:linear-gradient(180deg,#fff,#f3e9ec 50%,#fff)"></div>
    <div class="card-name">Lipbalm</div><div class="price">$ 30.00</div><div class="stars">★★★★★</div><div class="btn buy">Buy Now</div>
    <div class="abs quick" style="top:17px">
      <div class="icon-dot"><svg width="8" height="7" viewBox="0 0 10 9"><path d="M0 1h2l1.2 5h5L9.5 2.5H3" fill="none" stroke="#fff" stroke-width="1.3"/></svg></div>
      <div class="icon-dot"><svg width="8" height="7" viewBox="0 0 10 9"><path d="M5 8.5L1 4.6A2.3 2.3 0 0 1 5 1.8a2.3 2.3 0 0 1 4 2.8z" fill="#fff"/></svg></div>
      <div class="icon-dot"><svg width="9" height="6" viewBox="0 0 10 6"><path d="M.5 3Q5-2 9.5 3 5 8 .5 3z" fill="none" stroke="#fff"/><circle cx="5" cy="3" r="1.2" fill="#fff"/></svg></div>
    </div>
  </div>
  <div class="abs card" style="left:496px;top:678px;height:212px">
    <div class="shot" role="img" aria-label="Product photo: open tin of green beard balm" style="background:linear-gradient(135deg,#fff,#e4ecd9 50%,#eee)"></div>
    <div class="card-name">Beard Balm</div><div class="price">$ 30.00</div><div class="stars">★★★★★</div><div class="btn buy">Buy Now</div>
  </div>
  <div class="abs arrow" style="left:649px;top:815px"><svg width="7" height="8" viewBox="0 0 7 8"><path d="M2 1l3 3-3 3" fill="none" stroke="#fff" stroke-width="1.5"/></svg></div>

  <div class="abs section-title" style="top:986px">OUR <span>BADGES</span></div>
  <div class="abs badge" style="left:88px;top:1045px" role="img" aria-label="Taste icon">
    <svg width="36" height="36" viewBox="0 0 34 34" class="ico"><path d="M3 17c4-6 8-8 11-6 2-1 4-1 6 0 3-2 7 0 11 6-4 6-9 9-14 9S7 23 3 17z"/><path d="M3 17h28"/><path d="M13 17v3a4 4 0 0 0 8 0v-3"/></svg></div>
  <div class="abs badge" style="left:201px;top:1045px" role="img" aria-label="Smell icon">
    <svg width="36" height="36" viewBox="0 0 34 34" class="ico"><path d="M16 4c-1 8-7 13-7 19 0 3 2 4 4 4 1 2 6 2 8 0 2 0 4-1 4-4 0-6-6-11-7-19"/><path d="M14 23.5a2 2 0 0 0 2 1.5M20 23.5a2 2 0 0 1-2 1.5"/></svg></div>
  <div class="abs badge" style="left:314px;top:1045px" role="img" aria-label="Vision icon">
    <svg width="38" height="38" viewBox="0 0 34 34" class="ico"><path d="M2 17Q17 4 32 17 17 30 2 17z"/><circle cx="17" cy="17" r="6"/><circle cx="17" cy="17" r="2.5" fill="#fff"/></svg></div>
  <div class="abs badge" style="left:427px;top:1045px" role="img" aria-label="Touch icon">
    <svg width="36" height="36" viewBox="0 0 34 34" class="ico" style="stroke-width:1.6"><path d="M9 13a8 8 0 0 1 16 0M5.5 14a11.5 11.5 0 0 1 23 0M12.5 14a4.5 4.5 0 0 1 9 0"/><path d="M15 31V17a2 2 0 0 1 4 0v7l5 1c2 .5 3 2 2.5 4l-.5 2"/></svg></div>
  <div class="abs badge" style="left:538px;top:1045px" role="img" aria-label="Hearing icon">
    <svg width="36" height="36" viewBox="0 0 34 34" class="ico"><path d="M14 29c2 2 6 1 7-2 1-3 6-5 6-11a8 8 0 0 0-16 0"/><path d="M15 16a4 4 0 0 1 8 0c0 2-2 3-3 4"/><path d="M7 13c-2 3-2 6 0 9M3.5 11c-3 4-3 9 0 13"/></svg></div>
  <div class="abs badge-label" style="left:70px;top:1117px">Taste</div>
  <div class="abs badge-label" style="left:183px;top:1117px">Smell</div>
  <div class="abs badge-label" style="left:296px;top:1117px">Vision</div>
  <div class="abs badge-label" style="left:409px;top:1117px">Touch</div>
  <div class="abs badge-label" style="left:520px;top:1117px">Hearing</div>

  <div class="abs band" style="top:1230px"></div>
  <div class="abs card" style="left:52px;top:1197px;height:211px">
    <div class="shot" role="img" aria-label="Product photo: pink soap bar" style="background:linear-gradient(135deg,#fff,#f6dfe4 50%,#fff)"></div>
    <div class="card-name">Soap Bass</div><div class="price">$ 30.00</div><div class="stars">★★★★★</div><div class="btn buy">Buy Now</div>
  </div>
  <div class="abs card" style="left:200px;top:1182px;height:251px">
    <div class="shot" role="img" aria-label="Product photo: beeswax candle discs and honeycomb" style="background:linear-gradient(135deg,#fff,#fbe3a0 50%,#fff3d3)"></div>
    <div class="card-name">Candles</div><div class="price">$ 30.00</div><div class="stars">★★★★★</div><div class="btn buy">Buy Now</div>
    <div class="abs quick" style="top:17px">
      <div class="icon-dot"><svg width="8" height="7" viewBox="0 0 10 9"><path d="M0 1h2l1.2 5h5L9.5 2.5H3" fill="none" stroke="#fff" stroke-width="1.3"/></svg></div>
      <div class="icon-dot"><svg width="8" height="7" viewBox="0 0 10 9"><path d="M5 8.5L1 4.6A2.3 2.3 0 0 1 5 1.8a2.3 2.3 0 0 1 4 2.8z" fill="#fff"/></svg></div>
      <div class="icon-dot"><svg width="9" height="6" viewBox="0 0 10 6"><path d="M.5 3Q5-2 9.5 3 5 8 .5 3z" fill="none" stroke="#fff"/><circle cx="5" cy="3" r="1.2" fill="#fff"/></svg></div>
    </div>
  </div>
  <div class="abs card" style="left:347px;top:1197px;height:211px">
    <div class="shot" role="img" aria-label="Product photo: bowl of wax with green leaves" style="background:linear-gradient(135deg,#fff,#eef3dc 50%,#fdf0cf)"></div>
    <div class="card-name">wax taxts</div><div class="price">$ 30.00</div><div class="stars">★★★★★</div><div class="btn buy">Buy Now</div>
  </div>
  <div class="abs band-copy" style="left:512px;top:1300px;width:146px"><h3>Top Seller</h3><p>Lorem ipsum dolor sit amet, consectetur adipiscing elit, sed do eiusmod tempor incididunt ut</p></div>
  <div class="abs arrow" style="left:14px;top:1334px"><svg width="7" height="8" viewBox="0 0 7 8"><path d="M5 1L2 4l3 3" fill="none" stroke="#fff" stroke-width="1.5"/></svg></div>

  <div class="abs section-title" style="top:1505px">Testimonilas</div>
  <div class="abs quote-mark" style="left:122px;top:1528px">“</div>
  <div class="abs quote-mark" style="left:432px;top:1578px">”</div>
  <div class="abs quote-text">Lorem ipsum dolor sit amet, consectetur adipiscing elit, sed do eiusmod tempor incididunt ut labore et dolore magna aliqua. Ut enim ad minim veniam, quis nostrud exercitation ullamco laboris nisi ut aliquip ex ea commodo consequat.</div>
  <div class="abs avatar" style="left:290px;top:1614px;width:40px;height:40px;background:#d8dfe4" role="img" aria-label="Customer portrait"></div>
  <div class="abs avatar" style="left:336px;top:1609px;width:50px;height:50px;background:#b59a86;box-shadow:0 0 0 2px var(--purple)" role="img" aria-label="Customer portrait, selected"></div>
  <div class="abs avatar" style="left:391px;top:1613px;width:42px;height:42px;background:#c7ccd2" role="img" aria-label="Customer portrait"></div>
  <div class="abs person stars" style="top:1678px;margin:0">★★★★★</div>
  <div class="abs person" style="top:1694px;font-family:'Poppins',Arial,sans-serif;font-weight:700;font-size:9px">– Mara Quinn</div>
  <div class="abs person" style="top:1714px;font-size:8px">Lorem ipsum dolor sit</div>
  <div class="abs dots"><i></i><i class="on"></i><i></i></div>

  <div class="abs footer"></div>
  <div class="abs icon-dot" style="left:608px;top:1783px;width:27px;height:27px"><svg width="12" height="12" viewBox="0 0 12 12"><path d="M5 7L7 5M4.5 5.2L3 6.7a2 2 0 0 0 2.8 2.8L7.3 8M7.5 6.8L9 5.3A2 2 0 0 0 6.2 2.5L4.7 4" fill="none" stroke="#fff" stroke-width="1.3"/></svg></div>
  <div class="abs brand" style="left:64px;top:1832px;color:#fff"><span class="brand-dot"></span>LUMERA</div>
  <div class="abs f-text" style="left:63px;top:1865px;width:140px;color:#fff">Lorem ipsum dolor sit amet, consectetur adipiscing elit, sed do eiusmod tempor incididunt</div>
  <div class="abs f-head" style="left:226px;top:1825px;color:#fff">Using Links</div>
  <div class="abs f-list" style="left:228px;top:1843px;color:#fff"><div class="on">Home</div><div>Bath</div><div>Body</div><div>Face</div><div>Candles</div><div>Kids</div><div>Pets</div></div>
  <div class="abs f-head" style="left:332px;top:1825px;color:#fff">Contact US</div>
  <div class="abs contact" style="left:332px;top:1846px;color:#fff"><span class="icon-dot"></span><span>Lorem ipsum dolor<br>sit amet,&nbsp; 2503</span></div>
  <div class="abs contact" style="left:332px;top:1881px;color:#fff"><span class="icon-dot"></span><span>+ 888 888 8888</span></div>
  <div class="abs contact" style="left:332px;top:1908px;color:#fff"><span class="icon-dot"></span><span>info@lumeranaturals.com</span></div>
  <div class="abs f-head" style="left:485px;top:1825px;color:#fff">Lorem ipsum</div>
  <div class="abs f-search" style="color:#fff"><span>Search</span><svg width="7" height="7" viewBox="0 0 10 10"><circle cx="4" cy="4" r="3" fill="none" stroke="#fff" stroke-width="1.4"/><path d="M6.3 6.3L9 9" stroke="#fff" stroke-width="1.4"/></svg></div>
  <div class="abs f-head" style="left:485px;top:1881px;color:#fff">Follow Us</div>
  <div class="abs social" style="left:486px;top:1903px"></div>
  <div class="abs social" style="left:511px;top:1903px"></div>
  <div class="abs social" style="left:536px;top:1903px"></div>
  <div class="abs social" style="left:561px;top:1903px"></div>
  <div class="abs f-rule"></div>
  <div class="abs copy" style="color:#fff">©Copyrights 2022 Lumera Naturals | All Rights Reserved</div>
</div>

<!-- ============ HOME PAGE WITH OPEN MENU ============ -->
<div class="page page-menu">
  <div class="abs topbar">Lorem ipsum dolor sit amet, consectetur adipiscing elit, sed do eiusmod</div>
  <div class="abs brand header-brand"><span class="brand-dot"></span>LUMERA</div>
  <div class="abs search"><span>All Categories ⌄</span>
    <svg width="8" height="8" viewBox="0 0 10 10"><circle cx="4" cy="4" r="3" fill="none" stroke="#333" stroke-width="1.4"/><path d="M6.3 6.3L9 9" stroke="#333" stroke-width="1.4"/></svg></div>
  <div class="abs icon-dot" style="left:505px;top:42px"><svg width="9" height="8" viewBox="0 0 10 9"><path d="M5 8.5L1 4.6A2.3 2.3 0 0 1 5 1.8a2.3 2.3 0 0 1 4 2.8z" fill="#fff"/></svg></div>
  <div class="abs icon-dot" style="left:531px;top:42px"><svg width="9" height="8" viewBox="0 0 10 9"><path d="M0 1h2l1.2 5h5L9.5 2.5H3" fill="none" stroke="#fff" stroke-width="1.3"/></svg></div>
  <div class="abs btn login">LOG IN</div>
  <div class="abs rule"></div>
  <div class="abs nav active" style="left:177px">Home</div>
  <div class="abs nav" style="left:233px">Bath</div>
  <div class="abs nav" style="left:282px">Body</div>
  <div class="abs nav" style="left:332px">Face</div>
  <div class="abs nav" style="left:381px">Candles</div>
  <div class="abs nav" style="left:444px">Kids</div>
  <div class="abs nav" style="left:492px">Pets</div>

  <div class="abs hero" role="img" aria-label="Banner photo: bright bathroom with a freestanding tub, plant, towel and small side table"></div>
  <div class="abs arrow" style="left:17px;top:258px"><svg width="7" height="8" viewBox="0 0 7 8"><path d="M5 1L2 4l3 3" fill="none" stroke="#fff" stroke-width="1.5"/></svg></div>
  <div class="abs arrow" style="left:645px;top:258px"><svg width="7" height="8" viewBox="0 0 7 8"><path d="M2 1l3 3-3 3" fill="none" stroke="#fff" stroke-width="1.5"/></svg></div>

  <div class="abs section-title" style="top:480px">OUR <span>MANTRA</span></div>
  <div class="abs mantra-icon" style="left:115px;top:527px" role="img" aria-label="Relax icon">
    <svg width="42" height="42" viewBox="0 0 40 40"><circle cx="20" cy="8" r="4" fill="#fff"/><path d="M20 13c-4 0-6 3-6 8v4h12v-4c0-5-2-8-6-8z" fill="#fff"/><path class="ico" d="M14 17l-6 6 5 2M26 17l6 6-5 2"/><path d="M6 31c4-4 9-5 14-5s10 1 14 5c-5 2-9 2-14 1-5 1-9 1-14-1z" fill="#fff"/></svg></div>
  <div class="abs mantra-icon" style="left:305px;top:527px" role="img" aria-label="Re-energize icon">
    <svg width="44" height="44" viewBox="0 0 40 40" class="ico" style="stroke-width:1.6"><circle cx="24" cy="8" r="3"/><path d="M24 1.5v2M24 12.5v2M17.5 8h2M28.5 8h2M19.5 3.5l1.3 1.3M27.2 11.2l1.3 1.3M28.5 3.5l-1.3 1.3M19.5 12.5l1.3-1.3"/><path d="M9 22c0-3 2-4 4-4h14c2 0 4 1 4 4"/><path d="M5 22h30v5H5zM8 27v7M32 27v7M5 31h30"/></svg></div>
  <div class="abs mantra-icon" style="left:496px;top:527px" role="img" aria-label="Reinvent icon">
    <svg width="42" height="42" viewBox="0 0 40 40" class="ico" style="stroke-width:1.7"><path d="M20 4a11 11 0 0 0-6 20c1 1 2 3 2 5h8c0-2 1-4 2-5a11 11 0 0 0-6-20z"/><path d="M16 33h8M17 36h6"/><path d="M23 11.5c-.8-1-1.8-1.5-3-1.5-2 0-3 1-3 2.5 0 3.5 6 2 6 5.5 0 1.5-1.4 2.5-3 2.5-1.4 0-2.5-.6-3.3-1.5M20 7.5v2.5M20 20.5v2"/></svg></div>
  <div class="abs mantra-label" style="left:89px;top:596px"><b>Relax</b><small>Sustainably</small></div>
  <div class="abs mantra-label" style="left:279px;top:596px"><b>Re-Energize</b><small>Maskfully crafted</small></div>
  <div class="abs mantra-label" style="left:470px;top:596px"><b>Reinvent</b><small>Reinvent</small></div>

  <div class="abs band" style="top:710px"></div>
  <div class="abs band-copy" style="left:28px;top:780px;width:155px"><h3>Featured Products</h3><p>Lorem ipsum dolor sit amet, consectetur adipiscing elit, sed do eiusmod tempor incididunt ut labore et</p></div>
  <div class="abs card" style="left:200px;top:678px;height:212px">
    <div class="shot" role="img" aria-label="Product photo: coloured bath crayons" style="background:linear-gradient(135deg,#fff,#e9eef5 40%,#f6e7c3)"></div>
    <div class="card-name">Bath Caryans</div><div class="price">$ 30.00</div><div class="stars">★★★★★</div><div class="btn buy">Buy Now</div>
  </div>
  <div class="abs card" style="left:348px;top:663px;height:252px">
    <div class="shot" role="img" aria-label="Product photo: lipbalm tube" style="background:linear-gradient(180deg,#fff,#f3e9ec 50%,#fff)"></div>
    <div class="card-name">Lipbalm</div><div class="price">$ 30.00</div><div class="stars">★★★★★</div><div class="btn buy">Buy Now</div>
    <div class="abs quick" style="top:17px">
      <div class="icon-dot"><svg width="8" height="7" viewBox="0 0 10 9"><path d="M0 1h2l1.2 5h5L9.5 2.5H3" fill="none" stroke="#fff" stroke-width="1.3"/></svg></div>
      <div class="icon-dot"><svg width="8" height="7" viewBox="0 0 10 9"><path d="M5 8.5L1 4.6A2.3 2.3 0 0 1 5 1.8a2.3 2.3 0 0 1 4 2.8z" fill="#fff"/></svg></div>
      <div class="icon-dot"><svg width="9" height="6" viewBox="0 0 10 6"><path d="M.5 3Q5-2 9.5 3 5 8 .5 3z" fill="none" stroke="#fff"/><circle cx="5" cy="3" r="1.2" fill="#fff"/></svg></div>
    </div>
  </div>
  <div class="abs card" style="left:496px;top:678px;height:212px">
    <div class="shot" role="img" aria-label="Product photo: open tin of green beard balm" style="background:linear-gradient(135deg,#fff,#e4ecd9 50%,#eee)"></div>
    <div class="card-name">Beard Balm</div><div class="price">$ 30.00</div><div class="stars">★★★★★</div><div class="btn buy">Buy Now</div>
  </div>
  <div class="abs arrow" style="left:649px;top:815px"><svg width="7" height="8" viewBox="0 0 7 8"><path d="M2 1l3 3-3 3" fill="none" stroke="#fff" stroke-width="1.5"/></svg></div>

  <div class="abs section-title" style="top:986px">OUR <span>BADGES</span></div>
  <div class="abs badge" style="left:88px;top:1045px" role="img" aria-label="Taste icon">
    <svg width="36" height="36" viewBox="0 0 34 34" class="ico"><path d="M3 17c4-6 8-8 11-6 2-1 4-1 6 0 3-2 7 0 11 6-4 6-9 9-14 9S7 23 3 17z"/><path d="M3 17h28"/><path d="M13 17v3a4 4 0 0 0 8 0v-3"/></svg></div>
  <div class="abs badge" style="left:201px;top:1045px" role="img" aria-label="Smell icon">
    <svg width="36" height="36" viewBox="0 0 34 34" class="ico"><path d="M16 4c-1 8-7 13-7 19 0 3 2 4 4 4 1 2 6 2 8 0 2 0 4-1 4-4 0-6-6-11-7-19"/><path d="M14 23.5a2 2 0 0 0 2 1.5M20 23.5a2 2 0 0 1-2 1.5"/></svg></div>
  <div class="abs badge" style="left:314px;top:1045px" role="img" aria-label="Vision icon">
    <svg width="38" height="38" viewBox="0 0 34 34" class="ico"><path d="M2 17Q17 4 32 17 17 30 2 17z"/><circle cx="17" cy="17" r="6"/><circle cx="17" cy="17" r="2.5" fill="#fff"/></svg></div>
  <div class="abs badge" style="left:427px;top:1045px" role="img" aria-label="Touch icon">
    <svg width="36" height="36" viewBox="0 0 34 34" class="ico" style="stroke-width:1.6"><path d="M9 13a8 8 0 0 1 16 0M5.5 14a11.5 11.5 0 0 1 23 0M12.5 14a4.5 4.5 0 0 1 9 0"/><path d="M15 31V17a2 2 0 0 1 4 0v7l5 1c2 .5 3 2 2.5 4l-.5 2"/></svg></div>
  <div class="abs badge" style="left:538px;top:1045px" role="img" aria-label="Hearing icon">
    <svg width="36" height="36" viewBox="0 0 34 34" class="ico"><path d="M14 29c2 2 6 1 7-2 1-3 6-5 6-11a8 8 0 0 0-16 0"/><path d="M15 16a4 4 0 0 1 8 0c0 2-2 3-3 4"/><path d="M7 13c-2 3-2 6 0 9M3.5 11c-3 4-3 9 0 13"/></svg></div>
  <div class="abs badge-label" style="left:70px;top:1117px">Taste</div>
  <div class="abs badge-label" style="left:183px;top:1117px">Smell</div>
  <div class="abs badge-label" style="left:296px;top:1117px">Vision</div>
  <div class="abs badge-label" style="left:409px;top:1117px">Touch</div>
  <div class="abs badge-label" style="left:520px;top:1117px">Hearing</div>

  <div class="abs band" style="top:1230px"></div>
  <div class="abs card" style="left:52px;top:1197px;height:211px">
    <div class="shot" role="img" aria-label="Product photo: pink soap bar" style="background:linear-gradient(135deg,#fff,#f6dfe4 50%,#fff)"></div>
    <div class="card-name">Soap Bass</div><div class="price">$ 30.00</div><div class="stars">★★★★★</div><div class="btn buy">Buy Now</div>
  </div>
  <div class="abs card" style="left:200px;top:1182px;height:251px">
    <div class="shot" role="img" aria-label="Product photo: beeswax candle discs and honeycomb" style="background:linear-gradient(135deg,#fff,#fbe3a0 50%,#fff3d3)"></div>
    <div class="card-name">Candles</div><div class="price">$ 30.00</div><div class="stars">★★★★★</div><div class="btn buy">Buy Now</div>
    <div class="abs quick" style="top:17px">
      <div class="icon-dot"><svg width="8" height="7" viewBox="0 0 10 9"><path d="M0 1h2l1.2 5h5L9.5 2.5H3" fill="none" stroke="#fff" stroke-width="1.3"/></svg></div>
      <div class="icon-dot"><svg width="8" height="7" viewBox="0 0 10 9"><path d="M5 8.5L1 4.6A2.3 2.3 0 0 1 5 1.8a2.3 2.3 0 0 1 4 2.8z" fill="#fff"/></svg></div>
      <div class="icon-dot"><svg width="9" height="6" viewBox="0 0 10 6"><path d="M.5 3Q5-2 9.5 3 5 8 .5 3z" fill="none" stroke="#fff"/><circle cx="5" cy="3" r="1.2" fill="#fff"/></svg></div>
    </div>
  </div>
  <div class="abs card" style="left:347px;top:1197px;height:211px">
    <div class="shot" role="img" aria-label="Product photo: bowl of wax with green leaves" style="background:linear-gradient(135deg,#fff,#eef3dc 50%,#fdf0cf)"></div>
    <div class="card-name">wax taxts</div><div class="price">$ 30.00</div><div class="stars">★★★★★</div><div class="btn buy">Buy Now</div>
  </div>
  <div class="abs band-copy" style="left:512px;top:1300px;width:146px"><h3>Top Seller</h3><p>Lorem ipsum dolor sit amet, consectetur adipiscing elit, sed do eiusmod tempor incididunt ut</p></div>
  <div class="abs arrow" style="left:14px;top:1334px"><svg width="7" height="8" viewBox="0 0 7 8"><path d="M5 1L2 4l3 3" fill="none" stroke="#fff" stroke-width="1.5"/></svg></div>

  <div class="abs section-title" style="top:1505px">Testimonilas</div>
  <div class="abs quote-mark" style="left:122px;top:1528px">“</div>
  <div class="abs quote-mark" style="left:432px;top:1578px">”</div>
  <div class="abs quote-text">Lorem ipsum dolor sit amet, consectetur adipiscing elit, sed do eiusmod tempor incididunt ut labore et dolore magna aliqua. Ut enim ad minim veniam, quis nostrud exercitation ullamco laboris nisi ut aliquip ex ea commodo consequat.</div>
  <div class="abs avatar" style="left:290px;top:1614px;width:40px;height:40px;background:#d8dfe4" role="img" aria-label="Customer portrait"></div>
  <div class="abs avatar" style="left:336px;top:1609px;width:50px;height:50px;background:#b59a86;box-shadow:0 0 0 2px var(--purple)" role="img" aria-label="Customer portrait, selected"></div>
  <div class="abs avatar" style="left:391px;top:1613px;width:42px;height:42px;background:#c7ccd2" role="img" aria-label="Customer portrait"></div>
  <div class="abs person stars" style="top:1678px;margin:0">★★★★★</div>
  <div class="abs person" style="top:1694px;font-family:'Poppins',Arial,sans-serif;font-weight:700;font-size:9px">– Mara Quinn</div>
  <div class="abs person" style="top:1714px;font-size:8px">Lorem ipsum dolor sit</div>
  <div class="abs dots"><i></i><i class="on"></i><i></i></div>

  <div class="abs footer"></div>
  <div class="abs icon-dot" style="left:608px;top:1783px;width:27px;height:27px"><svg width="12" height="12" viewBox="0 0 12 12"><path d="M5 7L7 5M4.5 5.2L3 6.7a2 2 0 0 0 2.8 2.8L7.3 8M7.5 6.8L9 5.3A2 2 0 0 0 6.2 2.5L4.7 4" fill="none" stroke="#fff" stroke-width="1.3"/></svg></div>
  <div class="abs brand" style="left:64px;top:1832px;color:#fff"><span class="brand-dot"></span>LUMERA</div>
  <div class="abs f-text" style="left:63px;top:1865px;width:140px;color:#fff">Lorem ipsum dolor sit amet, consectetur adipiscing elit, sed do eiusmod tempor incididunt</div>
  <div class="abs f-head" style="left:226px;top:1825px;color:#fff">Using Links</div>
  <div class="abs f-list" style="left:228px;top:1843px;color:#fff"><div class="on">Home</div><div>Bath</div><div>Body</div><div>Face</div><div>Candles</div><div>Kids</div><div>Pets</div></div>
  <div class="abs f-head" style="left:332px;top:1825px;color:#fff">Contact US</div>
  <div class="abs contact" style="left:332px;top:1846px;color:#fff"><span class="icon-dot"></span><span>Lorem ipsum dolor<br>sit amet,&nbsp; 2503</span></div>
  <div class="abs contact" style="left:332px;top:1881px;color:#fff"><span class="icon-dot"></span><span>+ 888 888 8888</span></div>
  <div class="abs contact" style="left:332px;top:1908px;color:#fff"><span class="icon-dot"></span><span>info@lumeranaturals.com</span></div>
  <div class="abs f-head" style="left:485px;top:1825px;color:#fff">Lorem ipsum</div>
  <div class="abs f-search" style="color:#fff"><span>Search</span><svg width="7" height="7" viewBox="0 0 10 10"><circle cx="4" cy="4" r="3" fill="none" stroke="#fff" stroke-width="1.4"/><path d="M6.3 6.3L9 9" stroke="#fff" stroke-width="1.4"/></svg></div>
  <div class="abs f-head" style="left:485px;top:1881px;color:#fff">Follow Us</div>
  <div class="abs social" style="left:486px;top:1903px"></div>
  <div class="abs social" style="left:511px;top:1903px"></div>
  <div class="abs social" style="left:536px;top:1903px"></div>
  <div class="abs social" style="left:561px;top:1903px"></div>
  <div class="abs f-rule"></div>
  <div class="abs copy" style="color:#fff">©Copyrights 2022 Lumera Naturals | All Rights Reserved</div>

  <div class="abs dim"></div>

  <div class="abs mega">
    <div class="abs mega-col" style="left:63px;top:36px"><h4>Bath</h4><ul><li>Bath Salts</li><li>Soap Bass</li><li>Bath Bonbs</li><li>Shower Steamer</li></ul></div>
    <div class="abs mega-col" style="left:190px;top:36px"><h4>Body</h4><ul><li>Body Butter</li><li>Massage Butter</li></ul></div>
    <div class="abs mega-col" style="left:318px;top:36px"><h4>Face</h4><ul><li>Lip Balm</li><li>Beard Balm</li></ul></div>
    <div class="abs mega-col" style="left:445px;top:36px"><h4>Candles</h4><ul><li>Sap</li><li>Beeswax</li><li>Saplcocount</li><li>Wax taxts</li></ul></div>
    <div class="abs mega-col" style="left:63px;top:136px"><h4>Kids</h4><ul><li>Bath Crayans</li></ul></div>
    <div class="abs mega-col" style="left:190px;top:136px"><h4>Pets</h4><ul><li>Paw Mate</li></ul></div>
  </div>
</div>

</div>
</body>
</html>
```